Kindle Book Cover for Teen Financial Niche

Had a temporary cover done for the book but it needs a lot better cover now it is starting to get some traction.
The current book can be seen here:
https://www.brindlepost.com/dp/Q7K42WZ9RT
I am wanting something very different if possible. Please search books in the teen financial niche on Brindlepost and you will see that a lot of the covers are very similar in style.
I am looking for something different that will stand out in a crowded marketplace.
If you are putting someone on the cover please use a male character rather than a female one.
Thanks
Tobin

```html
<!DOCTYPE html>
<html lang="en">
<head>
<meta charset="UTF-8">
<title>Personal Finance Money Mastery – Book Cover</title>
<link rel="stylesheet" href="https://fonts.googleapis.com/css2?family=Chonburi&family=Alfa+Slab+One&family=Libre+Caslon+Text:wght@400&family=Archivo+Black&display=swap">
<style>
  :root {
    --page: #ffffff;
    --peach: #f9ddd0;
    --sand: #ece0cf;
    --mint: #6fd8bd;
    --mint-soft: #a9e0cf;
    --navy: #1f1a6b;
    --maroon: #8a1b1f;
    --orange: #f47b2f;
    --pig-light: #f6c7a9;
    --pig-mid: #ec9a78;
    --bill: #c9cdb4;
  }
  * { margin: 0; padding: 0; box-sizing: border-box; }
  html, body {
    width: 877px; height: 1200px; overflow: hidden;
    background: var(--page);
  }
  .canvas { position: relative; width: 877px; height: 1200px; }
  .cover {
    position: absolute; left: 87px; top: 68px;
    width: 700px; height: 1048px; overflow: hidden;
    background:
      radial-gradient(ellipse 60% 30% at 50% 100%, rgba(111,216,189,0.9), rgba(111,216,189,0) 100%),
      linear-gradient(180deg, var(--peach) 0%, var(--peach) 28%, var(--sand) 48%, var(--mint-soft) 70%, var(--mint) 90%, var(--mint-soft) 100%);
  }
  .title {
    position: absolute; left: 0; top: 0; width: 700px; height: 440px;
  }
  .title text { font-family: "Chonburi", serif; fill: var(--navy); }
  .title .tagline { font-family: "Alfa Slab One", serif; fill: var(--orange); }
  .roadmap {
    position: absolute; left: 0; top: 376px; width: 700px;
    text-align: center;
    font-family: "Libre Caslon Text", serif;
    font-size: 19px; line-height: 27.5px; letter-spacing: 0.2px;
    color: var(--maroon);
  }
  .roadmap .navy { color: var(--navy); }
  .illustration {
    position: absolute; left: 124px; top: 468px;
    width: 452px; height: 440px;
    border-radius: 48% 48% 44% 44%;
    background: radial-gradient(ellipse at 50% 45%, var(--pig-light) 0%, var(--pig-mid) 55%, var(--bill) 80%, rgba(201,205,180,0) 100%);
  }
  .audience {
    position: absolute; left: 0; top: 920px; width: 700px;
    display: flex; align-items: center; justify-content: center; gap: 10px;
    font-family: "Archivo Black", sans-serif; font-size: 23px; letter-spacing: 1px;
    color: var(--navy);
  }
  .audience .rule { width: 66px; height: 2px; background: var(--navy); }
  .author {
    position: absolute; left: 0; top: 958px; width: 700px;
    text-align: center;
    font-family: "Archivo Black", sans-serif; font-size: 56px; letter-spacing: 2px;
    color: var(--orange);
  }
</style>
</head>
<body>
<main class="canvas">
  <section class="cover">
    <svg class="title" viewBox="0 0 700 440" aria-label="Personal Finance: Money Mastery">
      <defs>
        <path id="finance-arc" d="M110 313 Q350 285 590 313"/>
        <path id="mastery-arc" d="M130 350 Q350 370 570 350"/>
      </defs>
      <text x="350" y="157" text-anchor="middle" font-size="150" textLength="575" lengthAdjust="spacingAndGlyphs">PERSONAL</text>
      <text font-size="150" textLength="470" lengthAdjust="spacingAndGlyphs">
        <textPath href="#finance-arc" startOffset="50%" text-anchor="middle">FINANCE</textPath>
      </text>
      <text class="tagline" font-size="48" textLength="440" lengthAdjust="spacingAndGlyphs">
        <textPath href="#mastery-arc" startOffset="50%" text-anchor="middle">Money Mastery</textPath>
      </text>
    </svg>

    <p class="roadmap">
      A ROADMAP TO: <span class="navy">EARNING POWER,</span><br>
      <span class="navy">BUDGETING,</span> WISE SPENDING, SAVING AND<br>
      <span class="navy">INVESTING</span>
    </p>

    <div class="illustration" role="img" aria-label="Illustration of a round piggy bank wrapped in dollar bills, wearing glasses and a red bow tie, holding a stack of cash, with coins at its feet"></div>

    <div class="audience">
      <span class="rule"></span>
      <span>FOR TEENS AND YOUND ADULTS</span>
      <span class="rule"></span>
    </div>

    <p class="author">LUCA MORETTI</p>
  </section>
</main>
</body>
</html>
```